An expert for Professional and Technical Evaluation of Painting Work Needs a New Letterhead Design

I own a mid-sized painting company and also work as an expert for professional and technical evaluation of painting work in the area of Zurich.

Please read the project description and the must-have-requirements carefully!

I attached 1 PDF which will help you create a new letterhead design:

THE NEW DESIGN DOESN'T NEED A LOGO! (Because it won't represent a company, it represents only a service)
Updates

Dear designers We had a discussion about the location/placement of the design and came to the conclusion that we only want the design to be in the header area of the A4-paper. We would be glad to receive some revised version of your designs. Thank you and kind regards!

Reason: Due to the fact that only 20% of the designer have understood the brief and submitted designs that have met the requirements we decided to extend the contest deadline.

Reason: A great deal of good designs were submitted in the last few days. A big thank you to all the participating designers for your good work. We need a few more days to discuss some changes with certain designers and to decide which design will win.

Target Market(s)

(Insurance) Companies, partly also private clients.

Industry/Entity Type

Painting

Colors

Designer to choose colors to be used in the design.

Requirements
Must have
• All information (text, phone numbers, ...) of the old design ("old_letterhead_design.pdf") has also to be in the new one. Additional to that there are a few changes:
The phone numbers "01 583 61 47" and "01 583 61 37" change to "044 583 61 47" and "044 583 61 37". And please mention also this email address: gutachten@holvantrek.example .

- The design should only be in the header-area of the A4-paper. An the background color of the A4-paper will be white.

- The design should consist of two designs. One for the first page and a smaller version of the design for the following pages.

- THE NEW DESIGN DOESN'T NEED A LOGO! You can make a design with geometric forms, ...

- The new design should have a juridical look. It should only contain colors like brown, fawn, black, light green, ...... colors which look serious/reliable.
Nice to have
• Geometric Forms, Symbols or other design elements.

- It would also be nice to have some design elements which emphasize the kind of work we are offering.

```html
<!DOCTYPE html>
<html lang="de">
<head>
<meta charset="utf-8">
<title>Briefkopf – Markus Brunner</title>
<link rel="stylesheet" href="https://fonts.googleapis.com/css2?family=Source+Sans+3:wght@400;600;700&display=swap">
<style>
  :root {
    --paper: #ffffff;
    --accent: #8a5a2e;
    --accent-light: #a7b48a;
    --ink: #2b2b2b;
    --ink-soft: #555555;
    --rule: #9a9a9a;
    --band-dark: #1f1d1a;
    --texture-light: #c9c3ad;
    --texture-dark: #a39c86;
  }
  html, body {
    margin: 0;
    padding: 0;
    width: 949px;
    height: 1200px;
    overflow: hidden;
    background: var(--paper);
  }
  .letterhead {
    position: relative;
    width: 949px;
    height: 1200px;
    background: var(--paper);
    font-family: "Source Sans 3", "Myriad Pro", Arial, sans-serif;
    color: var(--ink);
  }
  .header-image {
    position: absolute;
    left: 28px;
    top: 15px;
    width: 128px;
    height: 130px;
    background: linear-gradient(135deg, var(--texture-light), var(--texture-dark));
  }
  .sender {
    position: absolute;
    left: 168px;
    top: 57px;
    line-height: 1.35;
  }
  .sender-name {
    margin: 0;
    font-size: 17px;
    font-weight: 700;
    color: var(--accent);
  }
  .sender-title {
    margin: 0;
    font-size: 17px;
    font-weight: 400;
    color: var(--ink-soft);
  }
  .services {
    position: absolute;
    left: 680px;
    top: 19px;
    height: 123px;
    border-left: 2px solid var(--rule);
    padding-left: 20px;
    margin: 0;
    list-style: none;
  }
  .services li {
    position: relative;
    font-size: 17px;
    line-height: 24.5px;
    padding-left: 14px;
    color: var(--ink);
  }
  .services li::before {
    content: "";
    position: absolute;
    left: 0;
    top: 9px;
    width: 7px;
    height: 7px;
    background: var(--ink-soft);
  }
  .contact-line {
    position: absolute;
    left: 28px;
    top: 153px;
    display: flex;
    align-items: center;
    gap: 7px;
    font-size: 14px;
    line-height: 18px;
    color: var(--ink);
  }
  .contact-line svg { display: block; }
  .contact-line span { margin-right: 8px; }
  .header-band {
    position: absolute;
    left: 0;
    top: 176px;
    width: 949px;
    height: 36px;
  }
  .address {
    position: absolute;
    left: 640px;
    top: 176px;
    width: 309px;
    height: 36px;
    line-height: 36px;
    text-align: center;
    font-size: 16px;
    color: #ffffff;
  }
</style>
</head>
<body>
<div class="letterhead">
  <div class="header-image" role="img" aria-label="Foto einer hellen verputzten Wand mit regelmässig angeordneten quadratischen Öffnungen"></div>

  <div class="sender">
    <p class="sender-name">Markus Brunner</p>
    <p class="sender-title">Eidg. Dipl. Malermeister</p>
  </div>

  <ul class="services">
    <li>Gutachten</li>
    <li>Expertisen</li>
    <li>Devisierungen</li>
    <li>Farbberatungen</li>
    <li>Dekorative Gestaltungen</li>
  </ul>

  <div class="contact-line">
    <svg width="12" height="12" viewBox="0 0 12 12" aria-hidden="true">
      <path d="M3 1 L5 3.5 L4 5 Q5 7 7 8 L8.5 7 L11 9 L9.5 11 Q4 10.5 1 3 Z" fill="var(--accent)"/>
    </svg>
    <span>044 583 61 47</span>
    <svg width="14" height="12" viewBox="0 0 14 12" aria-hidden="true">
      <rect x="3" y="0.5" width="8" height="4" fill="var(--accent)"/>
      <rect x="0.5" y="4" width="13" height="7.5" rx="1" fill="var(--accent)"/>
      <rect x="3" y="7" width="8" height="2" fill="#ffffff"/>
    </svg>
    <span>044 583 61 37</span>
    <svg width="9" height="14" viewBox="0 0 9 14" aria-hidden="true">
      <rect x="0.5" y="0.5" width="8" height="13" rx="1.5" fill="var(--accent)"/>
      <rect x="2" y="2" width="5" height="5" fill="#ffffff"/>
    </svg>
    <span>079 412 90 35</span>
    <svg width="14" height="10" viewBox="0 0 14 10" aria-hidden="true">
      <rect x="0.5" y="0.5" width="13" height="9" fill="var(--accent)"/>
      <path d="M1 1 L7 6 L13 1" fill="none" stroke="#ffffff" stroke-width="1.2"/>
    </svg>
    <span>gutachten@holvantrek.example</span>
  </div>

  <svg class="header-band" viewBox="0 0 949 36" aria-hidden="true">
    <polygon points="0,18 614,18 598,36 0,36" fill="var(--band-dark)"/>
    <polygon points="0,15 616,15 614,18 0,18" fill="var(--accent-light)"/>
    <polygon points="640,0 949,0 949,36 606,36" fill="var(--accent)"/>
  </svg>
  <div class="address">Birkenweg 7, 8803 Seldwil</div>
</div>
</body>
</html>
```